Powerpoint Presentation design template

I am looking for a PPT presentation that show class and professionalism and in the same colour them as the logo. It should be simple, but yet classy and pro. The business is an oil and gas exploration and exploitation business. The business has nothing to do with solar panel and other renewable energies, so please no solar panel or wind farms in the background. It would be more oil rigs and LNG plant in the background of some slide templates...

oil and gas exploration and exploitation

```html
<!DOCTYPE html>
<html lang="en">
<head>
<meta charset="utf-8">
<title>Kivara Energy Presentation Template</title>
<link href="https://fonts.googleapis.com/css2?family=Poppins:wght@400;500;600;700;800&display=swap" rel="stylesheet">
<style>
:root{
  --blue:#1685c8;
  --blue-dk:#0f6fae;
  --green:#1fa84f;
  --teal:#14a07c;
  --ink:#2b2b2b;
  --grey:#7a7a7a;
  --line:#d8dde2;
  --panel:#eef0f2;
  --bg:#dcdde0;
}
*{box-sizing:border-box;margin:0;padding:0}
html,body{width:800px;height:1200px;overflow:hidden}
body{background:var(--bg);font-family:"Poppins",sans-serif;color:var(--ink);position:relative}
.slide{position:absolute;width:231px;height:130px;background:#fff;overflow:hidden;box-shadow:0 2px 5px rgba(0,0,0,.18)}
.abs{position:absolute}
.logo{position:absolute;display:flex;align-items:center;gap:3px}
.logo-dot{width:11px;height:11px;border-radius:50%;background:var(--green)}
.logo-name{font-weight:700;color:var(--blue);font-size:7px;line-height:.95;letter-spacing:.3px}
.logo.sm .logo-dot{width:5px;height:5px}
.logo.sm .logo-name{font-size:3.2px}
.logo.lg .logo-dot{width:20px;height:20px}
.logo.lg .logo-name{font-size:13px}
.foot{position:absolute;left:6px;right:6px;bottom:4px;height:8px}
.foot .logo{left:0;top:0}
.foot-line{position:absolute;left:22px;right:8px;top:5px;border-top:.5px solid var(--blue)}
.foot-copy{position:absolute;right:12px;top:1px;font-size:1.8px;color:var(--blue)}
.pg{position:absolute;right:0;top:1px;width:6px;height:6px;border-radius:50%;background:var(--blue);color:#fff;font-size:3px;text-align:center;line-height:6px}
.h-g{font-weight:700;color:var(--green);line-height:1}
.h-b{font-weight:800;color:var(--blue);line-height:1}
.tx{font-size:3px;color:var(--grey);line-height:1.35}
.tx-b{font-size:3.4px;font-weight:700;color:var(--ink)}
.web{position:absolute;font-size:4px;letter-spacing:1.3px;color:var(--blue);font-weight:500}
.photo{position:absolute}
.circle{border-radius:50%}
.ph-rig{background:linear-gradient(160deg,#2e7fbf,#1fa84f)}
.ph-site{background:linear-gradient(160deg,#9aa9b8,#3c4d5e)}
.ph-worker{background:linear-gradient(160deg,#4e5b66,#d8741f)}
.ph-sunset{background:linear-gradient(180deg,#f0a46a,#6e4a6b 70%,#2c3140)}
.ph-office{background:linear-gradient(160deg,#d9dde2,#8b8e93)}
.ph-tablet{background:linear-gradient(160deg,#efefef,#a89b8d)}
.ph-plant{background:linear-gradient(180deg,#8fc0e6,#2d4e74)}
.wedge-g{position:absolute;background:var(--green)}
.wedge-b{position:absolute;background:linear-gradient(180deg,#2aa5e0,#1674c0)}
table{border-collapse:collapse}
.mgmt-ring{position:absolute;left:87px;top:54px;width:64px;height:64px;border-radius:50%;background:conic-gradient(var(--teal) 0 25%,var(--blue) 0 50%,var(--teal) 0 75%,var(--blue) 0)}
.mgmt-split-v{position:absolute;left:118px;top:54px;width:1.5px;height:64px;background:#fff}
.mgmt-split-h{position:absolute;left:87px;top:85px;width:64px;height:1.5px;background:#fff}
.mgmt-core{position:absolute;left:103px;top:70px;width:32px;height:32px;border-radius:50%;background:#fff;display:flex;align-items:center;justify-content:center;text-align:center;font-size:5.5px;font-weight:700;line-height:1.05;z-index:2}
</style>
</head>
<body>

<!-- 1 Cover -->
<section class="slide" style="left:43px;top:38px">
  <div class="logo" style="left:12px;top:16px"><span class="logo-dot"></span><span class="logo-name">KIVARA<br>ENERGY</span></div>
  <div class="abs h-b" style="left:12px;top:58px;font-size:11px">BUSINESS</div>
  <div class="abs" style="left:12px;top:71px;font-size:4.3px;font-weight:700;color:var(--green)">Presentation Template</div>
  <p class="abs tx" style="left:12px;top:79px;width:55px;font-size:2.4px;color:var(--ink)">Short sample text for the printing and layout industry.</p>
  <div class="web" style="left:12px;top:116px">www.website.com</div>
  <div class="photo ph-rig" role="img" aria-label="Oil rig and offshore platform photo in green and blue tones" style="left:92px;top:0;width:150px;height:130px;border-radius:60px 0 0 60px"></div>
</section>

<!-- 2 Health and Safety -->
<section class="slide" style="left:287px;top:38px">
  <div class="wedge-g" style="left:0;top:28px;width:38px;height:52px;border-radius:0 40px 0 0"></div>
  <div class="wedge-b" style="left:0;top:80px;width:80px;height:50px;border-radius:0 50px 0 0"></div>
  <div class="photo ph-worker circle" role="img" aria-label="Worker in hard hat at a refinery" style="left:24px;top:20px;width:70px;height:70px;border:2px solid #fff"></div>
  <div class="logo" style="left:186px;top:7px"><span class="logo-dot" style="width:8px;height:8px"></span><span class="logo-name" style="font-size:4.8px">KIVARA<br>ENERGY</span></div>
  <div class="abs h-b" style="left:112px;top:36px;font-size:11px">Health<br>and Safety</div>
  <p class="abs tx" style="left:112px;top:63px;width:90px;font-size:3.6px;color:var(--ink)">Lorem ipsum dolor sit amet, quam erat volutpat. wisi it lob edo consequat. ore te feugait nulla facilisi.</p>
  <div class="web" style="left:172px;top:116px;font-size:3.4px">www.website.com</div>
</section>

<!-- 3 Financial Overview -->
<section class="slide" style="left:529px;top:38px">
  <div class="wedge-b" style="left:0;top:0;width:48px;height:40px;border-radius:0 0 40px 0"></div>
  <div class="wedge-g" style="left:0;top:40px;width:44px;height:50px;border-radius:0 0 40px 0"></div>
  <div class="photo ph-tablet circle" role="img" aria-label="Hands reviewing financial charts on a tablet" style="left:25px;top:25px;width:80px;height:80px;border:2px solid var(--blue)"></div>
  <div class="logo" style="left:186px;top:7px"><span class="logo-dot" style="width:8px;height:8px"></span><span class="logo-name" style="font-size:4.8px">KIVARA<br>ENERGY</span></div>
  <div class="abs h-b" style="left:112px;top:44px;font-size:11px;color:var(--green)">Financial<br><span style="color:var(--blue)">Overview</span></div>
  <p class="abs tx" style="left:112px;top:71px;width:90px;font-size:3.6px;color:var(--ink)">Lorem ipsum dolor sit amet, quam erat volutpat. wisi it lob edo consequat. ore te feugait nulla facilisi.</p>
  <div class="web" style="left:172px;top:116px;font-size:3.4px">www.website.com</div>
</section>

<!-- 4 Business Strategy -->
<section class="slide" style="left:43px;top:180px">
  <div class="wedge-g" style="left:0;top:28px;width:36px;height:50px;border-radius:0 40px 0 0"></div>
  <div class="wedge-b" style="left:0;top:78px;width:90px;height:52px;border-radius:0 50px 0 0"></div>
  <div class="photo ph-office circle" role="img" aria-label="Business team meeting around a screen" style="left:24px;top:20px;width:80px;height:80px;border:2px solid #fff"></div>
  <div class="logo" style="left:186px;top:7px"><span class="logo-dot" style="width:8px;height:8px"></span><span class="logo-name" style="font-size:4.8px">KIVARA<br>ENERGY</span></div>
  <div class="abs h-b" style="left:112px;top:36px;font-size:11px">Business<br>Strategy</div>
  <p class="abs tx" style="left:112px;top:63px;width:90px;font-size:3.6px;color:var(--ink)">Lorem ipsum dolor sit amet, quam erat volutpat. wisi it lob edo consequat. ore te feugait nulla facilisi.</p>
  <div class="web" style="left:172px;top:116px;font-size:3.4px">www.website.com</div>
</section>

<!-- 5 Table of Content -->
<section class="slide" style="left:287px;top:180px">
  <div class="abs h-g" style="left:26px;top:47px;font-size:6.5px;color:var(--blue);font-weight:500">TABLE OF</div>
  <div class="abs h-b" style="left:26px;top:55px;font-size:12px">CONTENT</div>
  <p class="abs tx" style="left:26px;top:70px;width:84px;font-size:2.6px">Lorem Ipsum is simply dummy text of the printing and typesetting industry, standard text since the 1500s.</p>
  <div class="abs" style="left:118px;top:28px;width:102px">
    <div style="position:relative;height:12.7px;border-bottom:.5px solid var(--blue);font-size:2.8px"><span style="position:absolute;left:5px;top:3px">Simple Text One</span><span style="position:absolute;left:0;top:4px;width:2px;height:2px;border-radius:50%;background:var(--teal)"></span><span style="position:absolute;right:0;top:3px;width:6px;height:6px;border-radius:50%;background:var(--blue);color:#fff;font-size:2.4px;text-align:center;line-height:6px">02</span></div>
    <div style="position:relative;height:12.7px;border-bottom:.5px solid var(--blue);font-size:2.8px"><span style="position:absolute;left:5px;top:3px">Simple Text Two</span><span style="position:absolute;left:0;top:4px;width:2px;height:2px;border-radius:50%;background:var(--teal)"></span><span style="position:absolute;right:0;top:3px;width:6px;height:6px;border-radius:50%;background:var(--blue);color:#fff;font-size:2.4px;text-align:center;line-height:6px">04</span></div>
    <div style="position:relative;height:12.7px;border-bottom:.5px solid var(--blue);font-size:2.8px"><span style="position:absolute;left:5px;top:3px">Simple Text Three</span><span style="position:absolute;left:0;top:4px;width:2px;height:2px;border-radius:50%;background:var(--teal)"></span><span style="position:absolute;right:0;top:3px;width:6px;height:6px;border-radius:50%;background:var(--blue);color:#fff;font-size:2.4px;text-align:center;line-height:6px">06</span></div>
    <div style="position:relative;height:12.7px;border-bottom:.5px solid var(--blue);font-size:2.8px"><span style="position:absolute;left:5px;top:3px">Simple Text Four</span><span style="position:absolute;left:0;top:4px;width:2px;height:2px;border-radius:50%;background:var(--teal)"></span><span style="position:absolute;right:0;top:3px;width:6px;height:6px;border-radius:50%;background:var(--blue);color:#fff;font-size:2.4px;text-align:center;line-height:6px">08</span></div>
    <div style="position:relative;height:12.7px;border-bottom:.5px solid var(--blue);font-size:2.8px"><span style="position:absolute;left:5px;top:3px">Simple Text Five</span><span style="position:absolute;left:0;top:4px;width:2px;height:2px;border-radius:50%;background:var(--teal)"></span><span style="position:absolute;right:0;top:3px;width:6px;height:6px;border-radius:50%;background:var(--blue);color:#fff;font-size:2.4px;text-align:center;line-height:6px">10</span></div>
    <div style="position:relative;height:12.7px;border-bottom:.5px solid var(--blue);font-size:2.8px"><span style="position:absolute;left:5px;top:3px">Simple Text Six</span><span style="position:absolute;left:0;top:4px;width:2px;height:2px;border-radius:50%;background:var(--teal)"></span><span style="position:absolute;right:0;top:3px;width:6px;height:6px;border-radius:50%;background:var(--blue);color:#fff;font-size:2.4px;text-align:center;line-height:6px">12</span></div>
  </div>
  <div class="foot"><div class="logo sm"><span class="logo-dot"></span><span class="logo-name">KIVARA<br>ENERGY</span></div><span class="foot-line"></span><span class="foot-copy">© COPYRIGHTS KIVARA ENERGY</span><span class="pg">2</span></div>
</section>

<!-- 6 Overview -->
<section class="slide" style="left:529px;top:180px">
  <div class="photo ph-site" role="img" aria-label="Pumpjack and two engineers in hard hats" style="left:118px;top:0;width:113px;height:70px;clip-path:polygon(0 0,100% 0,100% 100%,30% 100%)"></div>
  <div class="abs" style="left:110px;top:0;width:12px;height:70px;background:var(--teal);clip-path:polygon(0 0,40% 0,100% 100%,60% 100%)"></div>
  <div class="abs" style="left:16px;top:12px;font-size:2.8px">A BUSINESS TEXT HERE</div>
  <div class="abs h-g" style="left:16px;top:21px;font-size:6.5px">OVERVIEW OF</div>
  <div class="abs h-b" style="left:16px;top:29px;font-size:10.5px">KIVARA ENERGY</div>
  <p class="abs tx" style="left:16px;top:42px;width:90px">Lorem ipsum dolor amet consectetur adipisc eiusmod incididunt labore dolore magna ullamco aliqua commodo.</p>
  <div class="abs" style="left:16px;top:60px;width:85px">
    <div style="display:flex;gap:4px;margin-bottom:4px"><span style="flex:none;width:6px;height:6px;border-radius:50%;background:var(--teal)"></span><span class="tx" style="font-size:2.6px">Lorem Ipsum is simply dummy text of the print and typesetting magna aliqua.</span></div>
    <div style="display:flex;gap:4px;margin-bottom:4px"><span style="flex:none;width:6px;height:6px;border-radius:50%;background:var(--teal)"></span><span class="tx" style="font-size:2.6px">Lorem Ipsum is simply dummy text of the print and typesetting magna aliqua.</span></div>
    <div style="display:flex;gap:4px"><span style="flex:none;width:6px;height:6px;border-radius:50%;background:var(--teal)"></span><span class="tx" style="font-size:2.6px">Lorem Ipsum is simply dummy text of the print and typesetting magna aliqua.</span></div>
  </div>
  <div class="abs" style="left:112px;top:79px;width:6px;height:6px;background:var(--blue);border-radius:1.5px"></div>
  <div class="abs tx-b" style="left:121px;top:80px;font-size:2.8px">Write Simple Text</div>
  <p class="abs tx" style="left:112px;top:89px;width:48px;font-size:2.4px">Lorem Ipsum is simply dummy text a print and typeset industry since 1500s.</p>
  <div class="abs" style="left:169px;top:79px;width:6px;height:6px;background:var(--blue);border-radius:1.5px"></div>
  <div class="abs tx-b" style="left:178px;top:80px;font-size:2.8px">Write Simple Text</div>
  <p class="abs tx" style="left:169px;top:89px;width:48px;font-size:2.4px">Lorem Ipsum is simply dummy text a print and typeset industry since 1500s.</p>
  <div class="foot"><div class="logo sm"><span class="logo-dot"></span><span class="logo-name">KIVARA<br>ENERGY</span></div><span class="foot-line"></span><span class="foot-copy">© COPYRIGHTS KIVARA ENERGY</span><span class="pg">3</span></div>
</section>

<!-- 7 Executive Summary -->
<section class="slide" style="left:43px;top:322px">
  <div class="abs" style="left:14px;top:11px;font-size:3.2px">SUMMARY OF SERVICES OFFERED BY KIVARA ENERGY</div>
  <div class="abs h-g" style="left:14px;top:20px;font-size:7.5px">EXECUTIVE</div>
  <div class="abs h-b" style="left:14px;top:30px;font-size:12.5px">SUMMARY</div>
  <div class="abs" style="left:14px;top:54px;width:58px"><div class="tx-b">Project Problem</div><p class="tx" style="font-size:2.5px">Lorem ipsum dolor sit amet, cons ectetuer adipiscing elit, sed diam nonummy nibh euismod tincidunt.</p></div>
  <div class="abs" style="left:75px;top:54px;width:58px"><div class="tx-b">Project Solution</div><p class="tx" style="font-size:2.5px">Lorem ipsum dolor sit amet, cons ectetuer adipiscing elit, sed diam nonummy nibh euismod tincidunt.</p></div>
  <div class="abs" style="left:14px;top:80px;width:58px"><div class="tx-b">Project Problem</div><p class="tx" style="font-size:2.5px">Lorem ipsum dolor sit amet, cons ectetuer adipiscing elit, sed diam nonummy nibh euismod tincidunt.</p></div>
  <div class="abs" style="left:75px;top:80px;width:58px"><div class="tx-b">Project Solution</div><p class="tx" style="font-size:2.5px">Lorem ipsum dolor sit amet, cons ectetuer adipiscing elit, sed diam nonummy nibh euismod tincidunt.</p></div>
  <div class="abs" style="left:140px;top:32px;width:38px;height:36px;background:var(--blue);border-radius:4px 1px 1px 1px;color:#fff;padding:4px;font-size:2.6px"><b>PROBLEM</b><br>Lorem ipsum dolor sit amet, cons ectetuer.</div>
  <div class="abs" style="left:180px;top:32px;width:38px;height:36px;background:var(--teal);border-radius:1px 4px 1px 1px;color:#fff;padding:4px;font-size:2.6px"><b>SOLUTION</b><br>Lorem ipsum dolor sit amet, cons ectetuer.</div>
  <div class="abs" style="left:140px;top:70px;width:38px;height:36px;background:var(--teal);border-radius:1px 1px 1px 4px;color:#fff;padding:4px;font-size:2.6px"><b>MARKET</b><br>Lorem ipsum dolor sit amet, cons ectetuer.</div>
  <div class="abs" style="left:180px;top:70px;width:38px;height:36px;background:var(--blue);border-radius:1px 1px 4px 1px;color:#fff;padding:4px;font-size:2.6px"><b>MISSION</b><br>Lorem ipsum dolor sit amet, cons ectetuer.</div>
  <div class="foot"><div class="logo sm"><span class="logo-dot"></span><span class="logo-name">KIVARA<br>ENERGY</span></div><span class="foot-line"></span><span class="foot-copy">© COPYRIGHTS KIVARA ENERGY</span><span class="pg">4</span></div>
</section>

<!-- 8 Services Offered -->
<section class="slide" style="left:287px;top:322px">
  <div class="abs h-g" style="left:15px;top:13px;font-size:7px">SERVICES OFFERED</div>
  <div class="abs h-b" style="left:15px;top:23px;font-size:9px">BY KIVARA ENERGY</div>
  <div class="abs" style="left:20px;top:38px;width:196px;height:68px;background:var(--panel);border-radius:20px"></div>
  <div class="abs" style="left:118px;top:38px;width:1px;height:68px;background:#fff"></div>
  <div class="abs" style="left:20px;top:72px;width:196px;height:1px;background:#fff"></div>
  <div class="photo ph-sunset circle" role="img" aria-label="Pumpjack at sunset" style="left:26px;top:43px;width:24px;height:24px;border:1.5px solid var(--blue)"></div>
  <div class="abs" style="left:55px;top:47px;font-size:6px;line-height:1.1">Oil Exploration<br>and Production</div>
  <div class="photo ph-worker circle" role="img" aria-label="Partners shaking hands" style="left:123px;top:43px;width:24px;height:24px;border:1.5px solid var(--blue)"></div>
  <div class="abs" style="left:152px;top:46px;font-size:6px;line-height:1.1">Joint<br>Venture</div>
  <div class="photo ph-plant circle" role="img" aria-label="Gas flare at a plant" style="left:26px;top:77px;width:24px;height:24px;border:1.5px solid var(--blue)"></div>
  <div class="abs" style="left:55px;top:81px;font-size:6px;line-height:1.1">Gas<br>flare capture</div>
  <div class="photo ph-plant circle" role="img" aria-label="LNG tanks at a terminal" style="left:123px;top:77px;width:24px;height:24px;border:1.5px solid var(--blue)"></div>
  <div class="abs" style="left:152px;top:81px;font-size:6px;line-height:1.1">LNG Production<br>Facility</div>
  <div class="foot"><div class="logo sm"><span class="logo-dot"></span><span class="logo-name">KIVARA<br>ENERGY</span></div><span class="foot-line"></span><span class="foot-copy">© COPYRIGHTS KIVARA ENERGY</span><span class="pg">5</span></div>
</section>

<!-- 9 Oil Exploration -->
<section class="slide" style="left:529px;top:322px">
  <div class="abs h-g" style="left:11px;top:7px;font-size:7.5px">OIL EXPLORATION</div>
  <div class="abs h-b" style="left:11px;top:17px;font-size:9.5px">AND PRODUCTION</div>
  <div class="photo ph-sunset circle" role="img" aria-label="Pumpjack silhouette under a pink sky" style="left:14px;top:33px;width:78px;height:78px;border:2.5px solid var(--blue);box-shadow:0 0 0 2px #fff inset"></div>
  <div class="abs tx-b" style="left:103px;top:37px;font-size:5px">Lorem ipsum dolor.</div>
  <p class="abs tx" style="left:103px;top:45px;width:113px;font-size:2.6px">Lorem ipsum dolor sit amet, consectetuer adipiscing elit, sed diam nonummy nibh euismod tincidunt ut laoreet dolore magna aliquam erat volutpat. Ut wisi enim ad minim veniam, quis nostrud exerci tation ullamcorper suscipit lobortis nisl ut aliquip ex ea commodo consequat.<br><br>Duis autem vel eum iriure dolor in hendrerit in vulputate velit esse molestie consequat, vel illum dolore eu feugiat nulla facilisis at vero eros et accumsan.<br><br>Lorem ipsum dolor sit amet, cons ectetuer adipiscing elit, sed diam nonummy nibh euismod tincidunt ut laoreet dolore magna aliquam erat volutpat.</p>
  <div class="foot"><div class="logo sm"><span class="logo-dot"></span><span class="logo-name">KIVARA<br>ENERGY</span></div><span class="foot-line"></span><span class="foot-copy">© COPYRIGHTS KIVARA ENERGY</span><span class="pg">6</span></div>
</section>

<!-- 10 List of oil fields -->
<section class="slide" style="left:43px;top:465px">
  <div class="abs h-g" style="left:7px;top:9px;font-size:7.5px">SUMMARY</div>
  <div class="abs h-b" style="left:7px;top:19px;font-size:8.5px">LIST OF OIL FIELDS</div>
  <div class="abs" style="left:16px;top:36px;width:70px">
    <div style="margin-bottom:5px"><div class="tx-b" style="font-size:3px">◆ LOREM IPSUM</div><p class="tx" style="font-size:2.4px;padding-left:4px">Lorem ipsumectetuer adipiscing elit, sed diam nonummy nibh euismod.</p></div>
    <div style="margin-bottom:5px"><div class="tx-b" style="font-size:3px">◆ LOREM IPSUM</div><p class="tx" style="font-size:2.4px;padding-left:4px">Lorem ipsumectetuer adipiscing elit, sed diam nonummy nibh euismod.</p></div>
    <div style="margin-bottom:5px"><div class="tx-b" style="font-size:3px">◆ LOREM IPSUM</div><p class="tx" style="font-size:2.4px;padding-left:4px">Lorem ipsumectetuer adipiscing elit, sed diam nonummy nibh euismod.</p></div>
    <div><div class="tx-b" style="font-size:3px">◆ LOREM IPSUM</div><p class="tx" style="font-size:2.4px;padding-left:4px">Lorem ipsumectetuer adipiscing elit, sed diam nonummy nibh euismod.</p></div>
  </div>
  <table class="abs" style="left:95px;top:37px;width:120px;font-size:2.6px">
    <tr style="height:16px"><td style="border:.5px solid var(--blue);width:38px;font-weight:700;text-align:center;font-size:3px">LOREM IPSUM</td><td class="tx" style="border:.5px solid var(--blue);padding:1px 2px;font-size:2.2px">Lorem ipsumectetuer adipiscing elit, sed diam nonummy nibh euismod tincidunt.</td></tr>
    <tr style="height:16px"><td style="border:.5px solid var(--blue);font-weight:700;text-align:center;font-size:3px">LOREM IPSUM</td><td class="tx" style="border:.5px solid var(--blue);padding:1px 2px;font-size:2.2px">Lorem ipsumectetuer adipiscing elit, sed diam nonummy nibh euismod tincidunt.</td></tr>
    <tr style="height:16px"><td style="border:.5px solid var(--blue);font-weight:700;text-align:center;font-size:3px">LOREM IPSUM</td><td class="tx" style="border:.5px solid var(--blue);padding:1px 2px;font-size:2.2px">Lorem ipsumectetuer adipiscing elit, sed diam nonummy nibh euismod tincidunt.</td></tr>
    <tr style="height:16px"><td style="border:.5px solid var(--blue);font-weight:700;text-align:center;font-size:3px">LOREM IPSUM</td><td class="tx" style="border:.5px solid var(--blue);padding:1px 2px;font-size:2.2px">Lorem ipsumectetuer adipiscing elit, sed diam nonummy nibh euismod tincidunt.</td></tr>
  </table>
  <div class="foot"><div class="logo sm"><span class="logo-dot"></span><span class="logo-name">KIVARA<br>ENERGY</span></div><span class="foot-line"></span><span class="foot-copy">© COPYRIGHTS KIVARA ENERGY</span><span class="pg">7</span></div>
</section>

<!-- 11 Oil fields name and description -->
<section class="slide" style="left:287px;top:465px">
  <div class="abs h-g" style="left:11px;top:10px;font-size:7.5px">OIL FIELDS</div>
  <div class="abs h-b" style="left:11px;top:20px;font-size:8.5px">NAME AND DESCRIPTION</div>
  <p class="abs tx" style="left:11px;top:32px;width:205px;font-size:2.6px">Lorem ipsum dolor sit amet, consectetuer adipiscing elit, sed diam nonummy nibh euismod tincidunt ut laoreet dolore magna aliquam erat volutpat. Ut wisi enim ad minim veniam, quis nostrud exerci.</p>
  <div class="abs tx-b" style="left:16px;top:49px">Lorem ipsum dolor.</div>
  <p class="abs tx" style="left:16px;top:55px;width:100px;font-size:2.5px">Lorem ipsum dolor sit amet, consectetuer adipiscing elit, sed diam nonummy nibh euismod tincidunt ut laoreet dolore magna aliquam erat volutpat.</p>
  <table class="abs" style="left:16px;top:76px;width:102px;font-size:2.6px">
    <tr style="background:var(--teal);color:#fff;font-weight:700;font-size:3.2px;height:8px"><td style="padding:0 3px;width:32px">Main Text</td><td style="text-align:center">Main Text</td></tr>
    <tr style="height:11px"><td style="padding:0 3px;border:.5px solid var(--line);font-size:3px;color:var(--grey)">Text Here</td><td class="tx" style="border:.5px solid var(--line);padding:1px 2px;font-size:2px">Lorem ipsum dolor sit amet, consectetuer adipiscing elit sed diam nonummy.</td></tr>
    <tr style="height:11px"><td style="padding:0 3px;border:.5px solid var(--line);font-size:3px;color:var(--grey)">Text Here</td><td class="tx" style="border:.5px solid var(--line);padding:1px 2px;font-size:2px">Lorem ipsum dolor sit amet, consectetuer adipiscing elit sed diam nonummy.</td></tr>
  </table>
  <div class="photo ph-sunset" role="img" aria-label="Offshore oil platform at sunset" style="left:127px;top:46px;width:83px;height:63px"></div>
  <div class="foot"><div class="logo sm"><span class="logo-dot"></span><span class="logo-name">KIVARA<br>ENERGY</span></div><span class="foot-line"></span><span class="pg" style="background:none;color:var(--ink)">7</span></div>
</section>

<!-- 12 Partners -->
<section class="slide" style="left:529px;top:465px">
  <div class="abs h-g" style="left:11px;top:12px;font-size:6.5px">OVERVIEW OF</div>
  <div class="abs h-b" style="left:11px;top:21px;font-size:8px">KIVARA ENERGY PARTNERS</div>
  <div class="abs" style="left:20px;top:40px;width:37px;height:20px;border:.8px solid var(--blue);border-radius:4px"></div>
  <div class="abs" style="left:70px;top:40px;width:37px;height:20px;border:.8px solid var(--blue);border-radius:4px"></div>
  <div class="abs" style="left:120px;top:40px;width:37px;height:20px;border:.8px solid var(--blue);border-radius:4px"></div>
  <div class="abs" style="left:170px;top:40px;width:37px;height:20px;border:.8px solid var(--blue);border-radius:4px"></div>
  <div class="abs" style="left:18px;top:64px;width:42px"><div class="tx-b" style="font-size:3.2px">Lorem ipsum dolor.</div><p class="tx" style="font-size:2.2px">Lorem ipsumectetuer adipiscing elit, sed diam nonummy nibh euismod tincidunt.<br><br>Lorem ipsumectetuer adipiscing elit, sed diam nonummy nibh euismod.</p></div>
  <div class="abs" style="left:68px;top:64px;width:42px"><div class="tx-b" style="font-size:3.2px">Lorem ipsum dolor.</div><p class="tx" style="font-size:2.2px">Lorem ipsumectetuer adipiscing elit, sed diam nonummy nibh euismod tincidunt.<br><br>Lorem ipsumectetuer adipiscing elit, sed diam nonummy nibh euismod.</p></div>
  <div class="abs" style="left:118px;top:64px;width:42px"><div class="tx-b" style="font-size:3.2px">Lorem ipsum dolor.</div><p class="tx" style="font-size:2.2px">Lorem ipsumectetuer adipiscing elit, sed diam nonummy nibh euismod tincidunt.<br><br>Lorem ipsumectetuer adipiscing elit, sed diam nonummy nibh euismod.</p></div>
  <div class="abs" style="left:168px;top:64px;width:42px"><div class="tx-b" style="font-size:3.2px">Lorem ipsum dolor.</div><p class="tx" style="font-size:2.2px">Lorem ipsumectetuer adipiscing elit, sed diam nonummy nibh euismod tincidunt.<br><br>Lorem ipsumectetuer adipiscing elit, sed diam nonummy nibh euismod.</p></div>
  <div class="foot"><div class="logo sm"><span class="logo-dot"></span><span class="logo-name">KIVARA<br>ENERGY</span></div><span class="foot-line"></span><span class="foot-copy">© COPYRIGHTS KIVARA ENERGY</span><span class="pg">8</span></div>
</section>

<!-- 13 Mission & Values -->
<section class="slide" style="left:43px;top:606px">
  <div class="abs h-g" style="left:17px;top:13px;font-size:6.5px">KIVARA ENERGY</div>
  <div class="abs h-b" style="left:17px;top:22px;font-size:8.5px">MISSION &amp; VALUES</div>
  <p class="abs tx" style="left:17px;top:34px;width:90px;font-size:2.7px">Lorem ipsum dolor sit amet, cons ectetuer adipiscing elit, sed diam nonummy nibh euismod tincidunt ipsum dolor sit amet.</p>
  <div class="photo ph-plant" role="img" aria-label="Refinery plant with pipes under blue sky" style="left:17px;top:52px;width:86px;height:50px;border-radius:4px"></div>
  <div class="abs" style="left:112px;top:29px;width:103px;height:33px;background:var(--panel);border-radius:5px"></div>
  <div class="abs" style="left:112px;top:29px;width:25px;height:33px;background:var(--teal);border-radius:5px"></div>
  <div class="abs tx-b" style="left:143px;top:34px;font-size:4.2px">Mission</div>
  <p class="abs tx" style="left:143px;top:41px;width:68px;font-size:2.6px">Lorem ipsum dolor sit amet, cons ectetuer adipiscing elit, sed diam nonummy nibh euismod tincidunt.</p>
  <div class="abs" style="left:112px;top:69px;width:103px;height:33px;background:var(--panel);border-radius:5px"></div>
  <div class="abs" style="left:112px;top:69px;width:25px;height:33px;background:var(--blue);border-radius:5px"></div>
  <div class="abs tx-b" style="left:143px;top:74px;font-size:4.2px">Values</div>
  <p class="abs tx" style="left:143px;top:81px;width:68px;font-size:2.6px">Lorem ipsum dolor sit amet, cons ectetuer adipiscing elit, sed diam nonummy nibh euismod tincidunt.</p>
  <div class="foot"><div class="logo sm"><span class="logo-dot"></span><span class="logo-name">KIVARA<br>ENERGY</span></div><span class="foot-line"></span><span class="foot-copy">© COPYRIGHTS KIVARA ENERGY</span><span class="pg">9</span></div>
</section>

<!-- 14 H&S Strategy -->
<section class="slide" style="left:287px;top:606px">
  <div class="abs h-b" style="left:7px;top:9px;font-size:8px;color:var(--green)">KIVARA ENERGY HEALTH AND</div>
  <div class="abs h-b" style="left:7px;top:19px;font-size:8.5px">SAFETY STRATEGY</div>
  <div class="abs" style="left:22px;top:42px;display:flex;gap:4px">
    <div style="width:32px;height:50px;border:1.5px solid #222;border-radius:4px;padding:3px 2px;text-align:center"><div style="font-size:2.6px;font-weight:700;color:var(--teal)">IDEA</div><p class="tx" style="font-size:1.8px">Lorem ipsum dolor sit amet consectetuer adipiscing elit sed diam.</p></div>
    <div style="width:32px;height:50px;border:1.5px solid #222;border-radius:4px;padding:3px 2px;text-align:center"><div style="font-size:2.6px;font-weight:700;color:var(--teal)">PROMOTION</div><p class="tx" style="font-size:1.8px">Lorem ipsum dolor sit amet consectetuer adipiscing elit sed diam.</p></div>
    <div style="width:32px;height:50px;border:1.5px solid #222;border-radius:4px;padding:3px 2px;text-align:center"><div style="font-size:2.6px;font-weight:700;color:var(--teal)">GROWTH</div><p class="tx" style="font-size:1.8px">Lorem ipsum dolor sit amet consectetuer adipiscing elit sed diam.</p></div>
    <div style="width:32px;height:50px;border:1.5px solid #222;border-radius:4px;padding:3px 2px;text-align:center"><div style="font-size:2.6px;font-weight:700;color:var(--teal)">LOREM IPSUM</div><p class="tx" style="font-size:1.8px">Lorem ipsum dolor sit amet consectetuer adipiscing elit sed diam.</p></div>
    <div style="width:32px;height:50px;border:1.5px solid #222;border-radius:4px;padding:3px 2px;text-align:center"><div style="font-size:2.6px;font-weight:700;color:var(--teal)">LOREM IPSUM</div><p class="tx" style="font-size:1.8px">Lorem ipsum dolor sit amet consectetuer adipiscing elit sed diam.</p></div>
  </div>
  <div class="foot"><div class="logo sm"><span class="logo-dot"></span><span class="logo-name">KIVARA<br>ENERGY</span></div><span class="foot-line"></span><span class="foot-copy">© COPYRIGHTS KIVARA ENERGY</span><span class="pg">9</span></div>
</section>

<!-- 15 Environmental strategy -->
<section class="slide" style="left:529px;top:606px">
  <div class="abs" style="left:140px;top:0;width:91px;height:95px;background:#1f1f1f;clip-path:polygon(0 0,100% 0,100% 100%,0 100%,0 40%,20% 20%)"></div>
  <div class="photo ph-worker" role="img" aria-label="Smiling oil worker in hard hat and vest" style="left:149px;top:16px;width:82px;height:80px"></div>
  <div class="abs" style="left:118px;top:96px;width:113px;height:17px;background:var(--blue);display:flex;align-items:center;color:#fff;font-weight:700;font-size:8px">
    <span style="width:22px;height:17px;background:var(--teal)"></span><span style="margin-left:6px;width:42px;border-right:.8px solid #fff">100K</span><span style="margin-left:6px">+1M</span></div>
  <div class="abs" style="left:11px;top:10px;font-size:4.2px;font-weight:700">KIVARA ENERGY</div>
  <div class="abs h-g" style="left:11px;top:18px;font-size:7.5px">ENVIRONMENTAL</div>
  <div class="abs h-b" style="left:11px;top:28px;font-size:11px">STRATEGY</div>
  <p class="abs tx" style="left:11px;top:42px;width:85px;font-size:2.8px">Lorem ipsum dolor sit amet consect adipisc elit incididunt labore dolore aliqua.</p>
  <div class="abs" style="left:25px;top:64px;width:5px;height:5px;background:var(--teal);border-radius:1px"></div>
  <div class="abs tx-b" style="left:33px;top:63px;font-size:4.4px">Make Simple Text</div>
  <p class="abs tx" style="left:25px;top:71px;width:90px;font-size:2.3px">Nemo enim ipsam voluptatem quia voluptas aspernat fugit sed quia magni dolore ratione.</p>
  <div class="abs" style="left:25px;top:87px;width:5px;height:5px;background:var(--teal);border-radius:1px"></div>
  <div class="abs tx-b" style="left:33px;top:86px;font-size:4.4px">Make Simple Text</div>
  <p class="abs tx" style="left:25px;top:94px;width:90px;font-size:2.3px">Nemo enim ipsam voluptatem quia voluptas aspernat fugit sed quia magni dolore ratione.</p>
  <div class="foot"><div class="logo sm"><span class="logo-dot"></span><span class="logo-name">KIVARA<br>ENERGY</span></div><span class="foot-line"></span><span class="foot-copy">© COPYRIGHTS KIVARA ENERGY</span><span class="pg">10</span></div>
</section>

<!-- 16 Benefits to society -->
<section class="slide" style="left:43px;top:750px">
  <div class="photo ph-worker" role="img" aria-label="Worker in hard hat facing an industrial plant" style="left:20px;top:13px;width:86px;height:93px;border-radius:4px"></div>
  <div class="abs h-g" style="left:117px;top:17px;font-size:6.5px">BENEFITS</div>
  <div class="abs h-b" style="left:117px;top:25px;font-size:10px">TO SOCIETY</div>
  <div class="abs" style="left:119px;top:39px;font-size:2.8px;font-weight:600">(job creation, more revenue for the government, etc)</div>
  <div class="abs" style="left:119px;top:48px;width:100px">
    <div style="display:flex;gap:4px;margin-bottom:4px"><span style="flex:none;width:5px;height:5px;border:.7px solid var(--teal);border-radius:1px"></span><div><div class="tx-b" style="font-size:3px">Lorem ipsum dolor.</div><p class="tx" style="font-size:2.6px">Lorem ipsumectetuer adipiscing elit, sed diam nonummy nibh euismod tincidunt.</p></div></div>
    <div style="display:flex;gap:4px;margin-bottom:4px"><span style="flex:none;width:5px;height:5px;border:.7px solid var(--teal);border-radius:1px"></span><div><div class="tx-b" style="font-size:3px">Lorem ipsum dolor.</div><p class="tx" style="font-size:2.6px">Lorem ipsumectetuer adipiscing elit, sed diam nonummy nibh euismod tincidunt.</p></div></div>
    <div style="display:flex;gap:4px"><span style="flex:none;width:5px;height:5px;border:.7px solid var(--teal);border-radius:1px"></span><div><div class="tx-b" style="font-size:3px">Lorem ipsum dolor.</div><p class="tx" style="font-size:2.6px">Lorem ipsumectetuer adipiscing elit, sed diam nonummy nibh euismod tincidunt.</p></div></div>
  </div>
  <div class="foot"><div class="logo sm"><span class="logo-dot"></span><span class="logo-name">KIVARA<br>ENERGY</span></div><span class="foot-line"></span><span class="foot-copy">© COPYRIGHTS KIVARA ENERGY</span><span class="pg">11</span></div>
</section>

<!-- 17 Geographic coverage -->
<section class="slide" style="left:287px;top:750px">
  <div class="abs h-g" style="left:10px;top:9px;font-size:6.5px">KIVARA ENERGY</div>
  <div class="abs h-g" style="left:10px;top:17px;font-size:6.5px">GEOGRAPHIC COVERAGE</div>
  <div class="abs h-b" style="left:10px;top:26px;font-size:9px">IN CENTRAL AFRICA</div>
  <svg class="abs" style="left:19px;top:41px" width="80" height="70" viewBox="0 0 80 70">
    <path d="M4 0H62L68 4L62 8H4Z" fill="var(--teal)"/><circle cx="4" cy="4" r="4" fill="var(--teal)"/>
    <path d="M4 22H62L68 26L62 30H4Z" fill="var(--blue)"/><circle cx="4" cy="26" r="4" fill="var(--blue)"/>
    <path d="M4 44H62L68 48L62 52H4Z" fill="#3a3a3a"/><circle cx="4" cy="48" r="4" fill="#3a3a3a"/>
    <g font-family="Poppins, sans-serif" fill="#fff" font-weight="700"><text x="2.6" y="5.5" font-size="4">1</text><text x="2.4" y="27.5" font-size="4">2</text><text x="2.4" y="49.5" font-size="4">3</text>
    <text x="12" y="5" font-size="2.4">LOREM IPSUM</text><text x="12" y="27" font-size="2.4">LOREM IPSUM</text><text x="12" y="49" font-size="2.4">LOREM IPSUM</text></g>
    <g font-family="Poppins, sans-serif" fill="#7a7a7a" font-size="2.4"><text x="0" y="13">Lorem ipsum dolor sit amet, consectetur adipiscing</text><text x="0" y="16">elit, sed do eiusmod tempor.</text><text x="0" y="35">Lorem ipsum dolor sit amet, consectetur adipiscing</text><text x="0" y="38">elit, sed do eiusmod tempor.</text><text x="0" y="57">Lorem ipsum dolor sit amet, consectetur adipiscing</text><text x="0" y="60">elit, sed do eiusmod tempor.</text></g>
  </svg>
  <div class="photo" role="img" aria-label="Map of Africa with location pins in central Africa" style="left:132px;top:12px;width:88px;height:104px;background:radial-gradient(ellipse at 50% 45%,#e6e8ea 55%,#fff 72%)"></div>
  <div class="abs" style="left:123px;top:69px;font-size:7px;font-weight:700">+ 24530</div>
  <p class="abs tx" style="left:121px;top:79px;width:36px;font-size:2.2px;text-align:center;color:#aaa">Lorem ipsum is simply dummy text of the printing.</p>
  <div class="foot"><div class="logo sm"><span class="logo-dot"></span><span class="logo-name">KIVARA<br>ENERGY</span></div><span class="foot-line"></span><span class="foot-copy">© COPYRIGHTS KIVARA ENERGY</span><span class="pg">12</span></div>
</section>

<!-- 18 Shareholders -->
<section class="slide" style="left:529px;top:750px">
  <div class="abs h-g" style="left:8px;top:6px;font-size:6.5px">KIVARA ENERGY</div>
  <div class="abs h-b" style="left:8px;top:14px;font-size:9px">SHAREHOLDERS' STRUCTURE</div>
  <p class="abs tx" style="left:8px;top:26px;width:140px;font-size:2.7px;color:var(--ink)">Lorem ipsum dolor sit amet, cons ectetuer adipiscing sed diam nonummy nibh euismod tincidunt.Lorem ipsum dolor sit amet.</p>
  <svg class="abs" style="left:38px;top:40px" width="66" height="66" viewBox="-3 -3 66 66">
    <g stroke="#fff" stroke-width="1.5">
      <path d="M30 30L30 2A28 28 0 0 1 46.5 7.3Z" fill="var(--teal)"/>
      <path d="M30 30L46.5 7.3A28 28 0 0 1 58 30Z" fill="#3b3b3b"/>
      <path d="M30 30L58 30A28 28 0 0 1 21.3 56.6Z" fill="#a9abae"/>
      <path d="M30 30L21.3 56.6A28 28 0 0 1 30 2Z" fill="var(--blue)"/>
    </g>
    <g font-family="Poppins, sans-serif" font-weight="700" fill="#fff" font-size="3.8" text-anchor="middle">
      <text x="36.2" y="12.4">10%</text>
      <text x="47" y="23.4">15%</text>
      <text x="40.6" y="46">30%</text>
      <text x="13" y="29">45%</text>
    </g>
  </svg>
  <div class="abs" style="left:118px;top:40px;width:105px;font-size:2.8px">
    <div style="display:flex;gap:4px;align-items:center;margin-bottom:6px"><span style="flex:none;width:8px;height:8px;border-radius:50%;background:var(--blue);color:#fff;font-size:3px;text-align:center;line-height:8px">01</span><div><b>Shareholders Name</b><p class="tx" style="font-size:1.9px">Lorem ipsum dolor sit amet, consectetur adipiscing elit, sed do eiusmod tempor.</p></div></div>
    <div style="display:flex;gap:4px;align-items:center;margin-bottom:6px;padding-left:6px"><span style="flex:none;width:8px;height:8px;border-radius:50%;background:var(--teal);color:#fff;font-size:3px;text-align:center;line-height:8px">02</span><div><b>Shareholders Name</b><p class="tx" style="font-size:1.9px">Lorem ipsum dolor sit amet, consectetur adipiscing elit, sed do eiusmod tempor.</p></div></div>
    <div style="display:flex;gap:4px;align-items:center;margin-bottom:6px;padding-left:6px"><span style="flex:none;width:8px;height:8px;border-radius:50%;background:#3b3b3b;color:#fff;font-size:3px;text-align:center;line-height:8px">03</span><div><b>Shareholders Name</b><p class="tx" style="font-size:1.9px">Lorem ipsum dolor sit amet, consectetur adipiscing elit, sed do eiusmod tempor.</p></div></div>
    <div style="display:flex;gap:4px;align-items:center"><span style="flex:none;width:8px;height:8px;border-radius:50%;background:#a9abae;color:#fff;font-size:3px;text-align:center;line-height:8px">04</span><div><b>Shareholders Name</b><p class="tx" style="font-size:1.9px">Lorem ipsum dolor sit amet, consectetur adipiscing elit, sed do eiusmod tempor.</p></div></div>
  </div>
  <div class="foot"><div class="logo sm"><span class="logo-dot"></span><span class="logo-name">KIVARA<br>ENERGY</span></div><span class="foot-line"></span><span class="foot-copy">© COPYRIGHTS KIVARA ENERGY</span><span class="pg">13</span></div>
</section>

<!-- 19 Organisational structure -->
<section class="slide" style="left:43px;top:892px">
  <div class="abs h-g" style="left:6px;top:8px;font-size:7.5px">KIVARA ENERGY</div>
  <div class="abs h-b" style="left:6px;top:17px;font-size:9.5px">ORGANISATIONAL STRUCTURE</div>
  <p class="abs tx" style="left:6px;top:29px;font-size:2.7px;color:var(--ink)">Lorem ipsum dolor sit amet, cons ectetuer adipiscing elit, sed diam nonummy nibh euismod tincidunt</p>
  <svg class="abs" style="left:0;top:34px" width="231" height="85" viewBox="0 0 231 85">
    <g fill="none" stroke="#555" stroke-width=".5">
      <path d="M114 19V27M48 27H180M48 27V30M114 27V30M180 27V30"/>
      <path d="M48 48V52M36 52H60M36 52V55M60 52V55"/>
      <path d="M114 48V52M102 52H126M102 52V55M126 52V55"/>
      <path d="M180 48V52M168 52H192M168 52V55M192 52V55"/>
    </g>
    <circle cx="114" cy="9" r="8" fill="#d9dadc" stroke="var(--blue)" stroke-width="1.2"/>
    <g fill="#d9dadc" stroke="var(--teal)" stroke-width="1"><circle cx="48" cy="37" r="6.5"/><circle cx="114" cy="37" r="6.5"/><circle cx="180" cy="37" r="6.5"/></g>
    <g fill="#e4e5e7" stroke="#888" stroke-width=".5"><circle cx="36" cy="60" r="5"/><circle cx="60" cy="60" r="5"/><circle cx="102" cy="60" r="5"/><circle cx="126" cy="60" r="5"/><circle cx="168" cy="60" r="5"/><circle cx="192" cy="60" r="5"/></g>
    <g font-family="Poppins, sans-serif" font-size="1.8" font-weight="700" text-anchor="middle" fill="#222"><text x="114" y="21">NAME SURNAME</text><text x="48" y="47">NAME SURNAME</text><text x="114" y="47">NAME SURNAME</text><text x="180" y="47">NAME SURNAME</text>
    <text x="36" y="68">NAME SURNAME</text><text x="60" y="68">NAME SURNAME</text><text x="102" y="68">NAME SURNAME</text><text x="126" y="68">NAME SURNAME</text><text x="168" y="68">NAME SURNAME</text><text x="192" y="68">NAME SURNAME</text></g>
  </svg>
  <div class="foot"><div class="logo sm"><span class="logo-dot"></span><span class="logo-name">KIVARA<br>ENERGY</span></div><span class="foot-line"></span><span class="foot-copy">© COPYRIGHTS KIVARA ENERGY</span><span class="pg">14</span></div>
</section>

<!-- 20 Management -->
<section class="slide" style="left:287px;top:892px">
  <div class="abs h-g" style="left:10px;top:11px;font-size:6.5px">KIVARA ENERGY</div>
  <div class="abs h-b" style="left:10px;top:20px;font-size:10px">MANAGEMENT</div>
  <div class="mgmt-ring"></div>
  <div class="mgmt-split-v"></div>
  <div class="mgmt-split-h"></div>
  <div class="mgmt-core">Text<br>Added</div>
  <div class="abs" style="left:24px;top:40px;width:60px;text-align:right"><div class="tx-b" style="font-size:4px">Text Here</div><p class="tx" style="font-size:2.3px">Lorem ipsum dolor sit amet, consectetuer adipiscing elit, sed diammy nibh euismod tincidunt.</p></div>
  <div class="abs" style="left:24px;top:86px;width:60px;text-align:right"><div class="tx-b" style="font-size:4px">Text Here</div><p class="tx" style="font-size:2.3px">Lorem ipsum dolor sit amet, consectetuer adipiscing elit, sed diammy nibh euismod tincidunt.</p></div>
  <div class="abs" style="left:156px;top:40px;width:60px"><div class="tx-b" style="font-size:4px">Text Here</div><p class="tx" style="font-size:2.3px">Lorem ipsum dolor sit amet, consectetuer adipiscing elit, sed diammy nibh euismod tincidunt.</p></div>
  <div class="abs" style="left:156px;top:86px;width:60px"><div class="tx-b" style="font-size:4px">Text Here</div><p class="tx" style="font-size:2.3px">Lorem ipsum dolor sit amet, consectetuer adipiscing elit, sed diammy nibh euismod tincidunt.</p></div>
  <div class="foot"><div class="logo sm"><span class="logo-dot"></span><span class="logo-name">KIVARA<br>ENERGY</span></div><span class="foot-line"></span><span class="foot-copy">© COPYRIGHTS KIVARA ENERGY</span><span class="pg">15</span></div>
</section>

<!-- 21 Board of directors -->
<section class="slide" style="left:529px;top:892px">
  <div class="abs h-g" style="left:9px;top:12px;font-size:6.5px">KIVARA ENERGY</div>
  <div class="abs h-b" style="left:9px;top:21px;font-size:10px">BOARD OF DIRECTORS</div>
  <div class="abs" style="left:30px;top:37px;width:36px;height:38px;background:#d7d8da;border:2px solid #fff;box-shadow:0 0 0 .8px var(--blue),2px 2px 0 var(--blue)" role="img" aria-label="Portrait photo of director"></div>
  <div class="abs" style="left:97px;top:37px;width:36px;height:38px;background:#d7d8da;border:2px solid #fff;box-shadow:0 0 0 .8px var(--blue),2px 2px 0 var(--blue)" role="img" aria-label="Portrait photo of designer"></div>
  <div class="abs" style="left:164px;top:37px;width:36px;height:38px;background:#d7d8da;border:2px solid #fff;box-shadow:0 0 0 .8px var(--blue),2px 2px 0 var(--blue)" role="img" aria-label="Portrait photo of developer"></div>
  <div class="abs" style="left:18px;top:81px;width:60px;text-align:center"><div style="font-size:3.6px;font-weight:700;color:var(--blue)">LENA MORAY</div><div style="font-size:2.4px;font-weight:600">Managing Director</div><p class="tx" style="font-size:1.9px">Lorem text is simply dummy text of print and typeset industry.</p><div style="font-size:4px;color:var(--blue);letter-spacing:2px">●●●</div></div>
  <div class="abs" style="left:85px;top:81px;width:60px;text-align:center"><div style="font-size:3.6px;font-weight:700;color:var(--blue)">TOMAS EKWE</div><div style="font-size:2.4px;font-weight:600">UI/UX Designer</div><p class="tx" style="font-size:1.9px">Lorem text is simply dummy text of print and typeset industry.</p><div style="font-size:4px;color:var(--blue);letter-spacing:2px">●●●</div></div>
  <div class="abs" style="left:152px;top:81px;width:60px;text-align:center"><div style="font-size:3.6px;font-weight:700;color:var(--blue)">ADA BRENNER</div><div style="font-size:2.4px;font-weight:600">Web Developer</div><p class="tx" style="font-size:1.9px">Lorem text is simply dummy text of print and typeset industry.</p><div style="font-size:4px;color:var(--blue);letter-spacing:2px">●●●</div></div>
  <div class="foot"><div class="logo sm"><span class="logo-dot"></span><span class="logo-name">KIVARA<br>ENERGY</span></div><span class="foot-line"></span><span class="foot-copy">© COPYRIGHTS KIVARA ENERGY</span><span class="pg">16</span></div>
</section>

<!-- 22 Timeline -->
<section class="slide" style="left:43px;top:1035px">
  <div class="abs h-g" style="left:9px;top:9px;font-size:6.5px">KIVARA ENERGY PROJECT</div>
  <div class="abs h-b" style="left:9px;top:18px;font-size:10px">DEPLOYMENT TIMELINE</div>
  <svg class="abs" style="left:0;top:34px" width="231" height="86" viewBox="0 0 231 86">
    <g font-family="Poppins, sans-serif" text-anchor="middle">
      <g font-size="3.6" font-weight="600" fill="#222"><text x="42" y="5">Your Title</text><text x="116" y="5">Your Title</text><text x="190" y="5">Your Title</text><text x="79" y="70">Your Title</text><text x="153" y="70">Your Title</text></g>
      <g font-size="2.7" fill="#666"><text x="42" y="9">Refers to a good or</text><text x="42" y="12">service being offered</text><text x="116" y="9">Refers to a good or</text><text x="116" y="12">service being offered</text><text x="190" y="9">Refers to a good or</text><text x="190" y="12">service being offered</text><text x="79" y="74">Refers to a good or</text><text x="79" y="77">service being offered</text><text x="153" y="74">Refers to a good or</text><text x="153" y="77">service being offered</text></g>
    </g>
    <g stroke="#333" stroke-width=".6"><path d="M42 18V28M116 18V28M190 18V28M79 42V52M153 42V52"/></g>
    <g fill="#333"><circle cx="42" cy="18" r="1.2"/><circle cx="116" cy="18" r="1.2"/><circle cx="190" cy="18" r="1.2"/><circle cx="79" cy="52" r="1.2"/><circle cx="153" cy="52" r="1.2"/></g>
    <path d="M22 30H60L57 36L60 42H22L25 36Z" fill="var(--blue)"/>
    <path d="M62 30H97L94 36L97 42H62L65 36Z" fill="var(--teal)"/>
    <path d="M99 30H134L131 36L134 42H99L102 36Z" fill="var(--blue)"/>
    <path d="M136 30H171L168 36L171 42H136L139 36Z" fill="var(--teal)"/>
    <path d="M173 30H210L207 36L210 42H173L176 36Z" fill="var(--blue)"/>
    <g font-family="Poppins, sans-serif" font-size="4" font-weight="700" fill="#fff" text-anchor="middle"><text x="42" y="37.5">1990</text><text x="79" y="37.5">2001</text><text x="116" y="37.5">2007</text><text x="153" y="37.5">2012</text><text x="190" y="37.5">2020</text></g>
  </svg>
  <div class="foot"><div class="logo sm"><span class="logo-dot"></span><span class="logo-name">KIVARA<br>ENERGY</span></div><span class="foot-line"></span><span class="foot-copy">© COPYRIGHTS KIVARA ENERGY</span><span class="pg">17</span></div>
</section>

<!-- 23 Financial comments -->
<section class="slide" style="left:287px;top:1035px">
  <div class="abs h-g" style="left:7px;top:9px;font-size:6.5px">KIVARA ENERGY FINANCIAL OVERVIEW WITH</div>
  <div class="abs h-b" style="left:7px;top:18px;font-size:9px">COMMENTS ON THE FINANCIAL</div>
  <table class="abs" style="left:21px;top:36px;width:185px;font-size:2.6px;text-align:center">
    <tr style="height:10px;background:var(--teal);color:#fff;font-weight:600"><td style="background:#fff"></td><td>Your Text Here</td><td>Your Text Here</td><td>Your Text Here</td><td>Your Text Here</td></tr>
    <tr style="height:12px;border-bottom:.5px solid var(--line)"><td style="background:var(--blue);color:#fff;width:42px">You can replace this text</td><td>2020</td><td>1</td><td>50%</td><td>1250</td></tr>
    <tr style="height:12px;border-bottom:.5px solid var(--line)"><td style="background:var(--blue);color:#fff">You can replace this text</td><td>2021</td><td>2</td><td>50%</td><td>3623</td></tr>
    <tr style="height:12px;border-bottom:.5px solid var(--line)"><td style="background:var(--blue);color:#fff">You can replace this text</td><td>2022</td><td>3</td><td>12%</td><td>2569</td></tr>
    <tr style="height:12px;border-bottom:.5px solid var(--line)"><td style="background:var(--blue);color:#fff">You can replace this text</td><td>2023</td><td>4</td><td>65%</td><td>1020</td></tr>
    <tr style="height:12px;border-bottom:.5px solid var(--line)"><td style="background:var(--blue);color:#fff">You can replace this text</td><td>2024</td><td>5</td><td>65%</td><td>1020</td></tr>
  </table>
  <div class="foot"><div class="logo sm"><span class="logo-dot"></span><span class="logo-name">KIVARA<br>ENERGY</span></div><span class="foot-line"></span><span class="foot-copy">© COPYRIGHTS KIVARA ENERGY</span><span class="pg">18</span></div>
</section>

<!-- 24 Contact -->
<section class="slide" style="left:529px;top:1035px">
  <div class="logo lg" style="left:70px;top:18px"><span class="logo-dot"></span><span class="logo-name">KIVARA<br>ENERGY</span></div>
  <div class="abs" style="left:0;width:231px;top:52px;text-align:center;font-size:4.6px;font-weight:500;color:var(--teal)">EMPOWERED TO MAKE A LASTING IMPACT GLOBALLY</div>
  <div class="abs" style="left:16px;top:62px;width:198px;height:37px;background:var(--teal);border-radius:4px;color:#fff">
    <div style="text-align:center;font-weight:700;font-size:9.5px;margin-top:3px">CONTACT US</div>
    <div style="display:flex;justify-content:space-between;padding:3px 10px 0 20px;font-size:3px;line-height:1.2">
      <span>◉ Address Street Name<br>&nbsp;&nbsp;&nbsp;City Name, Country 000</span>
      <span>☎ (+000) 123 456 789<br>&nbsp;&nbsp;&nbsp;(+000) 123 456 789</span>
      <span>✉ info@example.com</span>
    </div>
  </div>
  <div class="web" style="left:0;width:231px;text-align:center;top:111px">www.website.com</div>
</section>

</body>
</html>
```